Social Media designs (LinkedIn banner, LinkedIn posts, Instagram)

Hello designers!
We are looking to create some more concepts for our social media identity for a search firm (recruitment company)
I have attached a "brand toolkit" that shows our brand, logo, colour scheme to guide you with regards to colours and identiy.

You will see in the brand toolkit there are some examples of;
- A LinkedIn banner for the company (page 23)
- Social Media posts for LinkedIn and Instagram (page 21)

What we are looking for...

We don't really like the current LinkedIn banner ideas. We would like to see more concepts that look more aesthetically pleasing - the current ideas look quite dull.

We DO like the social media post concepts but we would like to have more templates/options that we can use (similar themes)

We welcome submissions for Social Media designs that we can use with our company branding. Thank you for your work in advance!

```html
<!DOCTYPE html>
<html lang="en">
<head>
<meta charset="utf-8">
<title>Harwick Lane – Social Media Set</title>
<link href="https://fonts.googleapis.com/css2?family=Montserrat:wght@400;500;600;700;800&display=swap" rel="stylesheet">
<style>
  :root {
    --ink: #16302b;
    --green: #4a8a72;
    --mint: #dce8e3;
    --grey: #e2e2e2;
    --white: #ffffff;
    --cream: #e7e4da;
    --page: #ffffff;
  }
  * { margin: 0; padding: 0; box-sizing: border-box; }
  html, body { width: 766px; height: 1200px; overflow: hidden; background: var(--page); }
  body { position: relative; font-family: "Montserrat", Arial, sans-serif; color: var(--ink); }
  .piece { position: absolute; overflow: hidden; background: var(--white); box-shadow: 0 1px 6px rgba(0,0,0,.12); }
  .piece svg.shapes { position: absolute; inset: 0; width: 100%; height: 100%; }
  .brand-name { position: absolute; font-family: "Montserrat", Arial, sans-serif; font-weight: 700; line-height: 1.02; display: flex; align-items: center; gap: 8px; white-space: nowrap; }
  .brand-name .mark { width: 0.8em; height: 0.8em; background: currentColor; flex: none; }

  /* LinkedIn banner */
  .banner { left: 24px; top: 26px; width: 724px; height: 181px; }
  .banner .photo { position: absolute; left: 0; top: 0; width: 405px; height: 181px;
    background: linear-gradient(160deg, #e9e6df 0%, #cfc8bb 45%, #6f7a55 100%); }
  .banner .brand-name { left: 300px; top: 20px; font-size: 19px; color: var(--ink); }
  .banner .headline { position: absolute; left: 486px; top: 37px; font-weight: 800; font-size: 22px; line-height: 40.5px; letter-spacing: 0; white-space: nowrap; }
  .banner .headline .accent { color: var(--green); }

  /* Report cover */
  .cover { left: 24px; top: 229px; width: 493px; height: 617px; }
  .cover .brand-name { left: 61px; top: 60px; font-size: 36px; color: var(--ink); }
  .cover .photo-clip { fill: url(#cityGlow); }
  .cover .title { position: absolute; left: 21px; top: 323px; color: var(--white); font-weight: 700; font-size: 26px; line-height: 35.5px; white-space: nowrap; }
  .cover .intro { position: absolute; left: 21px; top: 444px; width: 190px; color: var(--white); font-size: 7.6px; line-height: 13.5px; }
  .cover .contact { position: absolute; left: 21px; top: 527px; display: flex; align-items: center; gap: 10px; color: var(--white); }
  .cover .contact svg { width: 22px; height: 22px; }
  .cover .contact small { display: block; font-size: 8px; font-weight: 600; }
  .cover .contact strong { display: block; font-size: 13px; font-weight: 600; line-height: 14px; }

  /* Instagram / LinkedIn post */
  .post { left: 24px; top: 884px; width: 548px; height: 286px; background: var(--ink); box-shadow: none; }
  .post .brand-name { left: 30px; top: 22px; font-size: 30px; color: var(--white); }
  .post .photo { position: absolute; left: 307px; top: 0; width: 241px; height: 242px;
    background: linear-gradient(140deg, #2c4a48 0%, #3e5b5a 40%, #8b8a78 75%, #3a5251 100%); }
  .post .tagline { position: absolute; left: 30px; top: 124px; color: var(--cream); font-weight: 500; font-size: 34px; line-height: 46px; white-space: nowrap; }
  .post .accent-bar { position: absolute; left: 0; bottom: 0; width: 157px; height: 44px; background: var(--green); }
</style>
</head>
<body>

  <section class="piece banner" aria-label="LinkedIn banner">
    <div class="photo" role="img" aria-label="Photo of a modern white gabled house with large glass windows"></div>
    <svg class="shapes" viewBox="0 0 724 181" aria-hidden="true">
      <polygon points="590,0 682,0 531,181 434,181" fill="var(--mint)"/>
    </svg>
    <div class="brand-name"><span class="mark"></span>Harwick<br>Lane</div>
    <h1 class="headline">CASE MANAGER<br><span class="accent">ENHANCED</span><br>DUE DILIGENCE</h1>
  </section>

  <section class="piece cover" aria-label="Executive hiring report cover">
    <svg class="shapes" viewBox="0 0 493 617" aria-hidden="true">
      <defs>
        <linearGradient id="cityGlow" x1="0" y1="0" x2="0" y2="1">
          <stop offset="0" stop-color="#e8d9c6"/>
          <stop offset=".45" stop-color="#d59a62"/>
          <stop offset="1" stop-color="#5a4a42"/>
        </linearGradient>
      </defs>
      <polygon points="267,198 493,100 493,408 267,506" fill="var(--grey)"/>
      <polygon class="photo-clip" points="231,241 460,143 460,451 231,549" role="img" aria-label="Photo of a city street between tall buildings at sunset"/>
      <polygon points="0,186 87,222 87,241 0,280" fill="var(--ink)"/>
      <polygon points="0,280 209,189 209,581 126,617 0,617" fill="var(--green)"/>
      <polygon points="270,589 454,509 454,617 270,617" fill="var(--ink)"/>
    </svg>
    <div class="brand-name"><span class="mark"></span>Harwick<br>Lane</div>
    <h2 class="title">Q2 2023<br>Exec Hiring<br>Report</h2>
    <p class="intro">Lorem ipsum dolor sit amet, consectetur adip-iscing elit sed eiusmod tempor incididunt</p>
    <div class="contact">
      <svg viewBox="0 0 24 24" aria-hidden="true"><path fill="#fff" d="M6.6 10.8a15 15 0 0 0 6.6 6.6l2.2-2.2c.3-.3.7-.4 1-.2 1.1.4 2.3.6 3.6.6.6 0 1 .4 1 1V20c0 .6-.4 1-1 1A17 17 0 0 1 3 4c0-.6.4-1 1-1h3.5c.6 0 1 .4 1 1 0 1.3.2 2.5.6 3.6.1.3 0 .7-.2 1z"/></svg>
      <div><small>More Info Call Us:</small><strong>+1 (555) 014 2290</strong></div>
    </div>
  </section>

  <section class="piece post" aria-label="Social media post">
    <div class="photo" role="img" aria-label="Photo of city office towers and a tram in muted teal tones"></div>
    <div class="brand-name"><span class="mark"></span>Harwick<br>Lane</div>
    <h2 class="tagline">Talent Knows<br>no borders</h2>
    <div class="accent-bar"></div>
  </section>

</body>
</html>
```